Business Card Design Project

I need a business card design for a new business called Tolland Insurance Services. I am a small insurance broker that will provide business insurance services mostly to contractors and small businesses. My business is all about customer service and assistance rather than being a price driven/focused business. I want my business card to be professional giving the impression that I am larger than one person but not a corporate company. I have attached a copy of my logo.
Updates

Hi all

I have been advised that I need to show the following info for compliance reasons on my card. It only has to be small.

Can you please include either front or back:

Tolland Insurance Services Pty Ltd [ABN 61827405193] AR No 586714 as Authorised Representative of Brackford Insurance Group Pty Ltd ACN 274 906 518 ABN 82 274 906 518 AFS Licence No 718264

Reason: I need a further change to be made to the design. I need the contact number of 1300476815 added to the business card.

Hi All

I need one last change made to the card.

Can you please include the phone number 1300476815 to the card. If possible can this be made fairly clear on the card, either large on the back or another design idea you may have.

Target Market(s)

30+ Professionals

Industry/Entity Type

Insurance

Requirements
Must have
• I want a double sided design. My details to go on the card are as follows:

Dylan Tolland QRPSUV (Snr Assoc.) CIP
Director
PO Box 872, Kestrelvale SA 5091
Phone: 0438 617 204
Fax 08 8397 2418
Email: dylan@tollandinsure.example
Website: http://www.tollandinsure.example
Twitter: Tollandinsure
Facebook: facebook.com/tollandinsure

```html
<!DOCTYPE html>
<html lang="en">
<head>
<meta charset="utf-8">
<title>Tolland Insurance Services – Business Card</title>
<link href="https://fonts.googleapis.com/css2?family=Quicksand:wght@500;600&family=Open+Sans:wght@600;700&display=swap" rel="stylesheet">
<style>
  :root {
    --backdrop: #0b0b0b;
    --card: #f1f0f0;
    --ink: #2b2a2b;
    --accent: #e52b2b;
    --rule: #a9a9a9;
    --muted: #6a6a6a;
  }
  * { box-sizing: border-box; margin: 0; padding: 0; }
  html, body {
    width: 1200px; height: 900px; overflow: hidden;
    background: var(--backdrop);
  }
  .stage { position: relative; width: 1200px; height: 900px; }
  .card {
    position: absolute; top: 288px; width: 567px; height: 324px;
    background: var(--card);
    color: var(--ink);
  }
  .card--front { left: 19px; }
  .card--back { left: 614px; }

  /* Front */
  .brand {
    position: absolute; left: 70px; top: 118px;
    display: flex; align-items: center; gap: 22px;
  }
  .brand__dot {
    width: 26px; height: 26px; border-radius: 50%;
    background: var(--accent); flex: none;
  }
  .brand__lockup { display: flex; flex-direction: column; align-items: center; }
  .brand__name {
    font-family: "Quicksand", sans-serif; font-weight: 600;
    font-size: 42px; line-height: 1; letter-spacing: 0.5px;
    color: var(--ink);
  }
  .tagline {
    display: flex; align-items: center; gap: 12px; margin-top: 10px;
    font-family: "Open Sans", sans-serif; font-weight: 600;
    font-size: 12.5px; letter-spacing: 2.2px; color: var(--ink);
    white-space: nowrap;
  }
  .tagline__rule { width: 30px; height: 1.5px; background: var(--ink); }
  .tagline__em { color: var(--accent); font-weight: 700; }

  /* Back */
  .person { position: absolute; left: 34px; top: 26px; font-family: "Open Sans", sans-serif; }
  .person__name { font-size: 14px; font-weight: 700; }
  .person__surname { color: var(--accent); }
  .person__role { font-size: 10.5px; font-weight: 700; margin-top: 2px; }

  .back-mark {
    position: absolute; left: 34px; top: 92px; width: 140px;
    display: flex; flex-direction: column; align-items: center; gap: 14px;
  }
  .back-mark__dot { width: 26px; height: 26px; border-radius: 50%; background: var(--accent); }
  .back-mark__name {
    font-family: "Quicksand", sans-serif; font-weight: 600;
    font-size: 36px; line-height: 1; color: var(--ink);
  }

  .contact {
    position: absolute; left: 192px; width: 342px;
    font-family: "Open Sans", sans-serif; font-weight: 700;
    font-size: 11.2px; line-height: 13.7px; color: var(--ink);
    white-space: nowrap;
  }
  .contact--postal { top: 104px; }
  .contact--online { top: 178px; }
  .contact .hl { color: var(--accent); }
  .divider { position: absolute; left: 192px; width: 342px; height: 1.5px; background: var(--rule); }
  .divider--first { top: 166px; }
  .divider--second { top: 231px; }

  .hotline {
    position: absolute; left: 192px; top: 242px;
    font-family: "Open Sans", sans-serif; font-weight: 700;
    font-size: 21px; line-height: 1; color: var(--ink);
    letter-spacing: 0.5px;
  }
  .hotline__num { color: var(--accent); }

  .compliance {
    position: absolute; left: 34px; right: 33px; top: 284px;
    font-family: "Open Sans", sans-serif; font-weight: 600;
    font-size: 7.5px; line-height: 10.5px; color: var(--muted);
  }
</style>
</head>
<body>
<main class="stage">
  <section class="card card--front" aria-label="Card front">
    <div class="brand">
      <span class="brand__dot"></span>
      <div class="brand__lockup">
        <span class="brand__name">tolland insurance</span>
        <div class="tagline">
          <span class="tagline__rule"></span>
          <span>Insurance advice you can <span class="tagline__em">trust</span></span>
          <span class="tagline__rule"></span>
        </div>
      </div>
    </div>
  </section>

  <section class="card card--back" aria-label="Card back">
    <div class="person">
      <p class="person__name">Dylan <span class="person__surname">Tolland</span></p>
      <p class="person__role">QRPSUV (Snr Assoc.) CIP Director</p>
    </div>

    <div class="back-mark">
      <span class="back-mark__dot"></span>
      <span class="back-mark__name">tolland</span>
    </div>

    <div class="contact contact--postal">
      <p>PO Box 872, Kestrelvale SA 5091</p>
      <p>Phone : 0438 617 204</p>
      <p>Fax 08 8397 2418</p>
      <p>Email : dylan@<span class="hl">tolland</span>insure.example</p>
    </div>
    <div class="divider divider--first"></div>
    <div class="contact contact--online">
      <p>Website : http://www.<span class="hl">tolland</span>insure.example</p>
      <p>Facebook : facebook.com/<span class="hl">tolland</span>insure</p>
      <p>Twitter : <span class="hl">Tolland</span>insure</p>
    </div>
    <div class="divider divider--second"></div>

    <p class="hotline">Call <span class="hotline__num">1300 476 815</span></p>

    <p class="compliance">Tolland Insurance Services Pty Ltd [ABN 61827405193] AR No 586714 as Authorised Representative of Brackford Insurance Group Pty Ltd ACN 274 906 518 ABN 82 274 906 518 AFS Licence No 718264</p>
  </section>
</main>
</body>
</html>
```